Swimming Pool Supply Company Business Cards

We need business cards designed for company. These need to be easy to edit so that we can fill in names, titles, and contact info for each person who works here.

Dalton R. Whitfield
Manager of Legal & Finance
K.L. Brisbane, Incorporated

4837 Grenway Avenue
Marlow Heights, PA 19243

E. dalton@klbrisbane-example.com
M. (215) 555-0173
O. (215) 555-0148

Contact Information for Business Card

Looking to upgrade current business cards with graphic that can be edited. Looking for fresh ideas for an age old industry.

Font styles to use
Serif
Sans Serif

Colors

Designer to choose colors to be used in the design.

Requirements
Must have
• Professional, fresh, unique but professional

```html
<!DOCTYPE html>
<html lang="en">
<head>
<meta charset="utf-8">
<title>Business Cards – K.L. Brisbane, Incorporated</title>
<link rel="stylesheet" href="https://fonts.googleapis.com/css2?family=Montserrat:wght@400;500;600;700;800&display=swap">
<style>
  :root {
    --page-bg: #eceff3;
    --card-white: #ffffff;
    --brand-blue: #1f5aa6;
    --back-blue: #3b70b2;
    --deep-blue: #1d5aa5;
    --aqua: #169fdb;
    --ink: #3a3a3a;
    --white: #ffffff;
  }
  * { box-sizing: border-box; margin: 0; padding: 0; }
  html, body { width: 1200px; height: 960px; overflow: hidden; }
  body {
    background: var(--page-bg);
    font-family: "Montserrat", sans-serif;
    position: relative;
  }
  .card {
    position: absolute;
    left: 240px;
    width: 720px;
    height: 412px;
    border-radius: 4px;
    overflow: hidden;
    box-shadow: 0 10px 28px rgba(20, 40, 80, 0.18);
  }

  /* Back of card */
  .card-back {
    top: 46px;
    background: var(--back-blue);
    color: var(--white);
    text-align: center;
  }
  .card-back .wordmark {
    margin-top: 96px;
    font-size: 84px;
    font-weight: 800;
    letter-spacing: 4px;
    line-height: 1;
  }
  .card-back .tagline {
    margin-top: 14px;
    font-size: 15px;
    font-weight: 700;
    letter-spacing: 2.4px;
  }
  .card-back .company {
    margin-top: 40px;
    font-size: 18px;
    font-weight: 700;
  }
  .card-back .address,
  .card-back .website {
    margin-top: 6px;
    font-size: 15px;
    font-weight: 400;
    letter-spacing: 0.5px;
  }

  /* Front of card */
  .card-front {
    top: 502px;
    background: var(--card-white);
  }
  .card-front .brand {
    position: absolute;
    left: 44px;
    top: 40px;
    color: var(--brand-blue);
  }
  .card-front .wordmark {
    font-size: 70px;
    font-weight: 800;
    letter-spacing: 3px;
    line-height: 1;
  }
  .card-front .tagline {
    margin-top: 10px;
    font-size: 12.5px;
    font-weight: 700;
    letter-spacing: 2.2px;
  }
  .card-front .wave {
    position: absolute;
    left: 0;
    top: 0;
    width: 720px;
    height: 412px;
  }
  .person {
    position: absolute;
    right: 40px;
    top: 218px;
    text-align: right;
    color: var(--ink);
  }
  .person .name {
    font-size: 29px;
    font-weight: 700;
    letter-spacing: 0.6px;
  }
  .person .title {
    margin-top: 2px;
    font-size: 16px;
    font-weight: 500;
    letter-spacing: 0.5px;
  }
  .contact {
    position: absolute;
    left: 40px;
    top: 300px;
    list-style: none;
    color: var(--white);
  }
  .contact li {
    display: flex;
    align-items: center;
    gap: 12px;
    font-size: 17px;
    font-weight: 500;
    letter-spacing: 0.6px;
    line-height: 28px;
  }
  .contact svg { width: 16px; height: 16px; flex: none; }
</style>
</head>
<body>

  <section class="card card-back" aria-label="Card back">
    <div class="wordmark">BRISBANE</div>
    <div class="tagline">SWIMMING POOLS, SUPPLIES &amp; ACCESSORIES</div>
    <div class="company">K.L. Brisbane, Incorporated</div>
    <div class="address">4837 Grenway Avenue, Marlow Heights, PA 19243</div>
    <div class="website">www.klbrisbane-example.com</div>
  </section>

  <section class="card card-front" aria-label="Card front">
    <svg class="wave" viewBox="0 0 720 412" aria-hidden="true">
      <path d="M70 236 C170 196 280 200 370 250 S570 345 720 330 L720 372 C570 385 450 335 360 282 C270 232 160 222 70 236 Z" fill="var(--aqua)"/>
      <path d="M0 262 C120 214 260 208 360 262 S560 362 720 352" fill="none" stroke="var(--white)" stroke-width="5"/>
      <path d="M0 278 C120 232 255 226 352 278 S555 378 720 372 L720 412 L0 412 Z" fill="var(--deep-blue)"/>
      <path d="M0 300 C110 260 240 255 340 300" fill="none" stroke="var(--white)" stroke-width="2" opacity="0.85"/>
    </svg>

    <div class="brand">
      <div class="wordmark">BRISBANE</div>
      <div class="tagline">SWIMMING POOLS, SUPPLIES &amp; ACCESSORIES</div>
    </div>

    <div class="person">
      <div class="name">Dalton R. Whitfield</div>
      <div class="title">Manager of Legal &amp; Finance</div>
    </div>

    <ul class="contact">
      <li>
        <svg viewBox="0 0 16 16" aria-hidden="true"><rect x="4" y="1" width="8" height="14" rx="1.5" fill="none" stroke="currentColor" stroke-width="1.5"/><line x1="7" y1="12.5" x2="9" y2="12.5" stroke="currentColor" stroke-width="1.5"/></svg>
        (215) 555-0173
      </li>
      <li>
        <svg viewBox="0 0 16 16" aria-hidden="true"><path d="M4 1.5 L6.5 4.5 L5 6.5 C6 8.5 7.5 10 9.5 11 L11.5 9.5 L14.5 12 L12.5 14.5 C7 14 2 9 1.5 3.5 Z" fill="currentColor"/></svg>
        (215) 555-0148
      </li>
      <li>
        <svg viewBox="0 0 16 16" aria-hidden="true"><rect x="1" y="3.5" width="14" height="9" fill="none" stroke="currentColor" stroke-width="1.3"/><path d="M1 3.5 L8 9 L15 3.5" fill="none" stroke="currentColor" stroke-width="1.3"/></svg>
        e.dalton@klbrisbane-example.com
      </li>
    </ul>
  </section>

</body>
</html>
```